Marwick Ostrand Law website for a law firm

modern clean website for a small boutique law firm. Based in Sacramento, CA and the Bay Area. Practice areas of Family Law, Civil litigation, and Criminal Defense. We already have a logo design as well as attorney pictures to include on page.
Would like images of California included on site.
Would like site to go with Logo that is already designed...blue/grey/white colors.

Industry/Entity Type

Law Firm

Number of Pages Required

5+ page

Requirements
Must have
• I already have several pages of content drafted. Just need the pages with images to input content. Must be clean and modern feel. Want it to reflect California and small boutique feel that is provided personalized legal attention.
• Must have a page where I can blog or post articles on.

```html
<!DOCTYPE html>
<html lang="en">
<head>
<meta charset="utf-8">
<title>Marwick Ostrand Law</title>
<link rel="stylesheet" href="https://fonts.googleapis.com/css2?family=Raleway:wght@300;400;500;600;700&display=swap">
<style>
:root{
  --blue:#3b7fd0;
  --blue-deep:#1f5fb0;
  --blue-band:#2a6cc4;
  --navy:#24466f;
  --ink:#222;
  --muted:#666;
  --line:#d9d9d9;
  --dark:#1d2024;
  --footer:#2a2d33;
  --white:#fff;
}
*{margin:0;padding:0;box-sizing:border-box}
html,body{width:1200px;height:3475px;overflow:hidden}
body{font-family:"Raleway",sans-serif;color:var(--ink);background:var(--white);position:relative}
.abs{position:absolute}
a{color:inherit;text-decoration:none}

.topbar{left:0;top:0;width:1200px;height:28px;background:var(--blue);color:#fff;font-size:12px}
.topbar .contact{left:86px;top:7px;display:flex;gap:48px}
.topbar .contact span{display:flex;align-items:center;gap:8px}
.topbar .social{right:86px;top:6px;display:flex;gap:8px}
.topbar .social i{width:16px;height:16px;border-radius:50%;background:#fff;display:block}

.nav{left:0;top:28px;width:1200px;height:65px;background:#fff;border-bottom:1px solid #eee}
.logo{left:86px;top:14px;font-size:34px;font-weight:500;color:var(--blue);letter-spacing:1px}
.menu{top:25px;font-size:13px;font-weight:500}
.btn-consult{left:968px;top:14px;width:144px;height:34px;border-radius:17px;background:#8a8d91;color:#fff;font-size:11px;display:flex;align-items:center;justify-content:center}

.hero{left:0;top:93px;width:1200px;height:500px;background:radial-gradient(ellipse at 35% 45%,#4a3a2a 0%,#20180f 40%,#060505 80%)}
.hero-text{right:88px;top:132px;text-align:right;color:#fff;font-size:30px;font-weight:300;line-height:50px}
.btn-hero{left:940px;top:394px;width:174px;height:60px;border-radius:30px;background:var(--blue);color:#fff;font-size:16px;display:flex;align-items:center;justify-content:center}

.quote{left:86px;top:526px;width:375px;height:503px;background:var(--blue);padding:0 38px}
.quote h2{color:#fff;font-weight:400;font-size:26px;text-align:center;height:70px;line-height:70px;border-bottom:1px solid rgba(255,255,255,.4);margin:0 -38px 34px}
.quote .field{height:44px;background:#fff;margin-bottom:18px;font-size:11px;color:#999;padding:13px 10px}
.quote .field.msg{height:92px}
.quote .submit{width:152px;height:44px;background:var(--navy);color:#fff;margin:28px auto 0;display:flex;align-items:center;justify-content:center;font-size:18px}

.about{left:480px;top:526px;width:632px;height:503px;background:#fff;border:1px solid var(--line);padding:58px 64px}
.about h2{font-size:36px;font-weight:400;margin-bottom:32px}
.about h3{font-size:15px;font-weight:600;line-height:28px;margin-bottom:18px}
.about p{font-size:12.5px;color:var(--muted);line-height:24px}
.btn-box{display:flex;align-items:center;justify-content:center;background:var(--blue);color:#fff;font-size:16px}

.band{left:0;width:1200px;background:linear-gradient(180deg,var(--blue-deep),var(--blue-band) 60%,#2f6fc0)}
.band h2{color:#fff;font-weight:400;font-size:34px;text-align:center}
.band .rule{width:50px;height:1px;background:#fff;margin:14px auto}
.band p{color:#fff;font-size:12.5px;text-align:center}

.card{top:1272px;width:325px;height:273px;background:#fff;border:1px solid var(--line);text-align:center}
.card .icon{width:84px;height:84px;border-radius:50%;background:var(--blue);margin:24px auto 22px;display:flex;align-items:center;justify-content:center}
.card h3{font-size:20px;font-weight:400}
.card .rule{width:40px;height:1px;background:#999;margin:10px auto}
.card p{font-size:12px;color:#444;line-height:19px;padding:0 50px}
.card .more{width:104px;height:32px;border:1px solid var(--blue);margin:14px auto 0;font-size:11px;display:flex;align-items:center;justify-content:center}

.testi{left:0;top:1630px;width:1200px;text-align:center}
.testi h2{font-size:27px;font-weight:400;letter-spacing:1px}
.avatar{border-radius:50%;background:radial-gradient(circle,#a89a88,#5a4d42)}
.testi .rule{position:absolute;left:158px;width:884px;height:1px;background:var(--line)}
.testi blockquote{position:absolute;left:0;width:1200px;top:206px;font-size:16px;color:#444}
.testi cite{position:absolute;left:0;width:1200px;top:252px;font-size:16px;color:#666}
.dots{left:572px;top:1963px;display:flex;gap:8px}
.dots i{width:9px;height:9px;border-radius:50%;background:#ccc;display:block}
.dots i.on{background:var(--blue)}

.blog{left:0;top:2018px;width:1200px;height:457px;background:radial-gradient(ellipse at 45% 70%,#3b3f45 0%,#1a1d21 55%,#0e1013 100%)}
.blog h2{position:absolute;left:86px;top:68px;color:#fff;font-size:31px;font-weight:400;line-height:56px;letter-spacing:1px}
.blog .rule{position:absolute;left:86px;top:190px;width:104px;height:2px;background:var(--blue)}
.blog p{position:absolute;left:86px;top:218px;width:440px;color:#fff;font-size:12.5px;line-height:27px}
.blog .btn-out{position:absolute;left:86px;top:352px;width:127px;height:44px;border:1px solid #fff;color:#fff;font-size:13px;display:flex;align-items:center;justify-content:center}
.post{left:582px;width:530px;height:94px;background:#fff;display:flex}
.post .date{width:62px;background:var(--blue);color:#fff;text-align:center;padding-top:10px}
.post .date b{display:block;font-size:32px;font-weight:600;line-height:36px}
.post .date span{font-size:16px}
.post .body{padding:14px 18px;font-size:11.5px;line-height:18px;color:#333}
.post .meta{font-size:10.5px;color:#888;margin-top:6px;display:flex;gap:26px}

.team-left{left:86px;top:2748px;width:440px}
.team-left h3{font-size:15px;font-weight:600;line-height:28px}
.team-left p{font-size:12.5px;color:var(--muted);line-height:24px;margin-top:6px}
.member{top:2669px;height:327px;background:#fff;border:1px solid var(--line);text-align:center}
.member .avatar{width:134px;height:134px;margin:32px auto 20px}
.member h4{font-size:21px;font-weight:400}
.member em{display:block;font-size:13px;color:#555;margin-top:8px}
.member .soc{display:inline-flex;gap:6px;background:var(--blue);padding:8px 12px;margin-top:16px}
.member .soc i{width:14px;height:14px;background:#fff;opacity:.85;display:block;border-radius:2px}

.footer{left:0;top:3082px;width:1200px;height:393px;background:var(--footer);color:#fff}
.flogo{left:144px;top:60px;font-size:30px;font-weight:500;border:2px solid #fff;padding:0 6px;line-height:34px}
.footer .about-f{left:144px;top:114px;width:240px;font-size:12.5px;line-height:24px}
.footer .ci{left:144px;font-size:12.5px;display:flex;gap:12px;align-items:center}
.footer h5{font-size:12px;font-weight:500;letter-spacing:1px}
.footer .ul{width:36px;height:2px;background:var(--blue);margin-top:6px}
.gallery{left:466px;top:3174px;display:grid;grid-template-columns:repeat(3,74px);gap:14px 16px}
.gallery div{height:51px}
.news{left:850px;top:3180px;width:146px;height:38px;background:transparent;border:1px solid #666;font-size:11px;color:#888;padding:11px 10px}
.go{left:1002px;top:3180px;width:54px;height:38px;background:var(--blue);font-size:14px;font-weight:600;display:flex;align-items:center;justify-content:center}
.follow{left:856px;top:3300px;display:flex;gap:32px}
.follow i{width:18px;height:18px;border-radius:50%;background:#fff;display:block}
.copy{left:0;top:3415px;width:1200px;border-top:1px solid #3b3e44;text-align:center;font-size:11px;padding-top:22px;color:#ddd}
</style>
</head>
<body>

<div class="abs topbar">
  <div class="abs contact">
    <span><svg width="14" height="14" viewBox="0 0 14 14"><circle cx="7" cy="7" r="7" fill="#fff"/><rect x="3.5" y="4.5" width="7" height="5" fill="none" stroke="#3b7fd0"/><path d="M3.5 4.5 7 7.5 10.5 4.5" fill="none" stroke="#3b7fd0"/></svg>info@marwickostrand.com</span>
    <span><svg width="14" height="14" viewBox="0 0 14 14"><circle cx="7" cy="7" r="7" fill="#fff"/><rect x="5" y="3" width="4" height="8" rx="1" fill="#3b7fd0"/></svg>(888) 555-0142</span>
  </div>
  <div class="abs social"><i></i><i></i><i></i><i></i></div>
</div>

<header class="abs nav">
  <div class="abs logo">MOLAW</div>
  <a class="abs menu" style="left:465px">ABOUT US</a>
  <a class="abs menu" style="left:600px">PRACTICE AREAS</a>
  <a class="abs menu" style="left:775px">TEAM</a>
  <a class="abs menu" style="left:878px">CONTACT</a>
  <a class="abs btn-consult">FREE CONSULTATION</a>
</header>

<section class="abs hero" role="img" aria-label="Stack of old law books beside a globe in dim light"></section>
<div class="abs hero-text">WE HAVE BEEN IN THIS FIELD<br>SINCE1964<br>EXPERIENCE ON ALL KIND</div>
<a class="abs btn-hero">LEARN MORE</a>

<form class="abs quote">
  <h2>GET A FREE QUOTE</h2>
  <div class="field">Name..</div>
  <div class="field">Email..</div>
  <div class="field">Phone Number..</div>
  <div class="field msg">Message..</div>
  <div class="submit">SUBMIT</div>
</form>

<section class="abs about">
  <h2>ABOUT MO LAW</h2>
  <h3>HARBORLINE CLAIM SERVICES IS PROUD TO OFFER<br>EXPERT INSURANCE CLAIMS</h3>
  <p>Harborline Claim Services is proud to offer expert processing services to all of South Florida including the Miami Dade, Broward, West Palm Beach, Marco Island, and Naples areas. We have years of experience filing insurance claims in Miami and the surrounding areas of Ft. Lauderdale, Sunrise, and Boca Raton. If you're in need of assistance filing your insurance claim and you live in Aventura, Sunny Isles Beach, Hollywood, Surfside, Bal Harbour, Bay Harbor, or Miami Beach we're ready to start working for you. Our best-in-class public.</p>
  <a class="btn-box" style="width:152px;height:44px;margin-top:40px">LEARN MORE</a>
</section>

<section class="abs band" style="top:1103px;height:232px;padding-top:30px" role="img" aria-label="Faint blue-tinted city skyline">
  <h2>PRACTICE AREAS</h2>
  <div class="rule"></div>
  <p>Lorem ipsum dolor sit amet, consectetur adipiscing elit. Curabitur auctor mauris metus, sit amet porttitor dolor.</p>
</section>

<div class="abs card" style="left:86px">
  <div class="icon"><svg width="44" height="44" viewBox="0 0 44 44" fill="none" stroke="#fff" stroke-width="2"><circle cx="15" cy="13" r="5"/><circle cx="29" cy="13" r="5"/><path d="M6 36v-8a9 9 0 0 1 18 0v8M20 36v-8a9 9 0 0 1 18 0v8"/></svg></div>
  <h3>FAMILY LAW</h3><div class="rule"></div>
  <p>Lorem Ipsum is simply dummy text of the printing and typesetting industry.</p>
  <a class="more">LEARN MORE</a>
</div>
<div class="abs card" style="left:436px">
  <div class="icon"><svg width="44" height="44" viewBox="0 0 44 44" fill="none" stroke="#fff" stroke-width="2"><path d="M22 6v32M12 38h20M8 12h28M8 12l-5 12h10zM36 12l-5 12h10z"/></svg></div>
  <h3>CIVIL LITIGATION</h3><div class="rule"></div>
  <p>Lorem Ipsum is simply dummy text of the printing and typesetting industry.</p>
  <a class="more">LEARN MORE</a>
</div>
<div class="abs card" style="left:788px">
  <div class="icon"><svg width="44" height="44" viewBox="0 0 44 44" fill="none" stroke="#fff" stroke-width="2"><rect x="10" y="8" width="22" height="28" transform="rotate(-12 21 22)"/><path d="M15 16h12M15 22h12M15 28h8" transform="rotate(-12 21 22)"/></svg></div>
  <h3>CRIMINAL DEFENSE</h3><div class="rule"></div>
  <p>Lorem Ipsum is simply dummy text of the printing and typesetting industry.</p>
  <a class="more">LEARN MORE</a>
</div>

<section class="abs testi">
  <h2>WHAT OUR CLIENT SAYS</h2>
  <div class="abs avatar" style="left:557px;top:80px;width:86px;height:86px" role="img" aria-label="Client portrait"></div>
  <div class="rule" style="top:177px"></div>
  <blockquote>"It takes on average 150 hours of development to deliver 1 hr of training at $6,000!"</blockquote>
  <cite>Redfield Alliance</cite>
  <div class="rule" style="top:298px"></div>
</section>
<div class="abs dots"><i></i><i class="on"></i><i></i></div>

<section class="abs blog" role="img" aria-label="Dark photo of a gavel and chains">
  <h2>READ OUR EXPERTLY<br>WRITTEN BLOG</h2>
  <div class="rule"></div>
  <p>Lorem Ipsum is simply dummy text of the printing and typesetting industry. Lorem Ipsum has been the industry's standard dummy text ever since the 1500s, when an unknown printer took a galley of type and scrambled it to .</p>
  <a class="btn-out">LEARN MORE</a>
</section>
<article class="abs post" style="top:2064px"><div class="date"><b>18</b><span>JAN</span></div><div class="body">Lorem Ipsum is simply dummy text of the printing and typesetting industry. has been the industry's standard dummy text ever since the 1500s.<div class="meta"><span>◷ 23rd may 2016</span><span>▢ 0 comments</span></div></div></article>
<article class="abs post" style="top:2201px"><div class="date"><b>25</b><span>JAN</span></div><div class="body">Lorem Ipsum is simply dummy text of the printing and typesetting industry. has been the industry's standard dummy text ever since the 1500s.<div class="meta"><span>◷ 23rd may 2016</span><span>▢ 0 comments</span></div></div></article>
<article class="abs post" style="top:2338px"><div class="date"><b>30</b><span>JAN</span></div><div class="body">Lorem Ipsum is simply dummy text of the printing and typesetting industry. has been the industry's standard dummy text ever since the 1500s.<div class="meta"><span>◷ 23rd may 2016</span><span>▢ 0 comments</span></div></div></article>

<section class="abs band" style="top:2498px;height:224px;padding-top:36px" role="img" aria-label="Faint blue-tinted city skyline">
  <h2>OUR TEAM</h2>
  <div class="rule"></div>
  <p>Lorem ipsum dolor sit amet, consectetur adipiscing elit. Curabitur auctor mauris metus, sit amet porttitor dolor.</p>
</section>
<div class="abs team-left">
  <h3>HARBORLINE CLAIM SERVICES IS PROUD TO<br>OFFER</h3>
  <p>Harborline Claim Services is proud to offer expert processing services to all of South Florida including the Miami Dade, Broward, West Palm Beach, Marco Island, and Naples areas. We have years of experience filing insurance claims in Miami and the surrounding areas of Ft. Lauderdale, Sunrise, and Boca Raton.</p>
</div>
<a class="abs btn-box" style="left:83px;top:2952px;width:153px;height:46px">LEARN MORE</a>
<div class="abs member" style="left:614px;width:239px">
  <div class="avatar" role="img" aria-label="Portrait of Maren T. Ostrand"></div>
  <h4>MAREN T. OSTRAND</h4><em>SENIOR PARTNER</em>
  <div class="soc"><i></i><i></i><i></i><i></i></div>
</div>
<div class="abs member" style="left:878px;width:234px">
  <div class="avatar" role="img" aria-label="Portrait of Owen S. Marwick"></div>
  <h4>OWEN S. MARWICK</h4><em>SENIOR PARTNER</em>
  <div class="soc"><i></i><i></i><i></i><i></i></div>
</div>

<footer class="abs footer">
  <div class="abs flogo">MOLAW</div>
  <p class="abs about-f">Lorem Ipsum is simply dummy text of the printing and typesetting industry.</p>
  <div class="abs ci" style="top:200px"><svg width="12" height="12" viewBox="0 0 12 12"><path d="M2 1l3 0 1 3-1.5 1a6 6 0 0 0 2.5 2.5L8 6l3 1v3a1 1 0 0 1-1 1A9 9 0 0 1 1 2a1 1 0 0 1 1-1z" fill="#3b7fd0"/></svg>(219) 555-0187</div>
  <div class="abs ci" style="top:232px"><svg width="12" height="10" viewBox="0 0 12 10"><rect width="12" height="10" fill="#3b7fd0"/><path d="M0 0l6 5 6-5" fill="none" stroke="#2a2d33"/></svg>info@marwickostrand.com</div>
  <div class="abs" style="left:466px;top:52px"><h5>OUR GALLERY</h5><div class="ul"></div></div>
  <div class="abs" style="left:850px;top:52px"><h5>NEWSLETTER</h5><div class="ul"></div></div>
  <div class="abs" style="left:850px;top:170px"><h5>FOLLOW US</h5><div class="ul"></div></div>
</footer>
<div class="abs gallery">
  <div role="img" aria-label="Handcuffs" style="background:linear-gradient(135deg,#6b4a38,#2e2420)"></div>
  <div role="img" aria-label="Signing a contract" style="background:linear-gradient(135deg,#b89a84,#5d4a40)"></div>
  <div role="img" aria-label="Handshake over desk" style="background:linear-gradient(135deg,#e4d8cc,#9a7a62)"></div>
  <div role="img" aria-label="Legal documents" style="background:linear-gradient(135deg,#9fb8d8,#e8eef6)"></div>
  <div role="img" aria-label="Courthouse columns" style="background:linear-gradient(135deg,#c6ccd4,#6a7480)"></div>
  <div role="img" aria-label="Meeting with lawyer" style="background:linear-gradient(135deg,#3a3c44,#85807a)"></div>
  <div role="img" aria-label="Court building facade" style="background:linear-gradient(135deg,#d8dce2,#7c8590)"></div>
  <div role="img" aria-label="Lawyer in dark suit" style="background:linear-gradient(135deg,#1c1e22,#55585e)"></div>
  <div role="img" aria-label="Scales of justice" style="background:linear-gradient(135deg,#a8c4e0,#e6eef7)"></div>
</div>
<div class="abs news">Your Email id....</div>
<div class="abs go" style="color:#fff">GO</div>
<div class="abs follow"><i></i><i></i><i></i><i></i></div>
<div class="abs copy">marwickostrand.com2017. All rights reserved</div>

</body>
</html>
```